Maple Nest Child Care & Preschool - Need a flyer template

I would like to design an 8 x 10 flyer . We are a child care center. I want the flyer to be a template that can be used to create 1, 2 or 4 page flyers for the center. The final design should communicate happy children and educate the parent on why they should choose us. I want it simple enough so that if I want to move something around and create a new page, it will be relative easy. Colorful block areas where words can be placed. A footer at the bottom with contact info.

Target Market(s)

Target market is women with children between the ages of 18 and 60. Mothers and grandmothers

Industry/Entity Type

Childcare

Font styles to use
Sans Serif

Colors
fbed22
ec1f27
3176b5

Requirements
Must have
• It would be nice to match the colors of the logo. It doesn't have to be limited but the logo colors should be the main colors. It should have contact info and such on the 1st page. The template should have a second page that can add expanded info. See the Harbor Method 2nd page or the Tiny Oaks 2-4 pages. The first is more of a cover-1 page flyer and then I may add additional info(4 page could be to send via email).
Nice to have
• Nice would be some stock photos of children of all colors. We are 65% African American, 30% White, 5% Hispanic
Should not have
• Not sure.

```html
<!DOCTYPE html>
<html lang="en">
<head>
<meta charset="utf-8">
<title>Maple Nest Child Care &amp; Preschool – Flyer</title>
<link rel="stylesheet" href="https://fonts.googleapis.com/css2?family=Fredoka:wght@500;600;700&family=Open+Sans:wght@300;400;600;700;800&display=swap">
<style>
  :root{
    --yellow:#fbed22;
    --gold:#f7c51c;
    --red:#ec1f27;
    --blue:#3176b5;
    --blue-deep:#1f62a8;
    --blue-bright:#2a8ad0;
    --white:#ffffff;
    --page-bg:#e4e4e4;
  }
  html,body{margin:0;padding:0;overflow:hidden;}
  body{width:1200px;height:840px;background:var(--page-bg);position:relative;font-family:"Open Sans",sans-serif;}
  .flyer{
    position:absolute;left:288px;top:30px;width:624px;height:780px;
    background:linear-gradient(160deg,var(--blue-bright) 0%,var(--blue) 55%,var(--blue-deep) 100%);
    overflow:hidden;box-shadow:0 6px 18px rgba(0,0,0,.18);
  }
  .top-rule{position:absolute;left:0;top:0;width:100%;height:8px;background:var(--gold);}
  .logo-box{
    position:absolute;left:0;top:8px;width:250px;height:92px;background:var(--white);
    display:flex;align-items:center;gap:10px;padding-left:22px;box-sizing:border-box;
    border-left:14px solid var(--blue);
  }
  .logo-dot{width:24px;height:24px;border-radius:50%;background:var(--gold);flex:none;}
  .logo-name{font-weight:700;color:var(--blue);font-size:13px;line-height:1.25;white-space:nowrap;}
  .header{position:absolute;left:250px;top:8px;right:0;height:92px;padding:12px 20px 0 24px;box-sizing:border-box;color:var(--white);}
  .header .lead{font-weight:300;font-size:18px;color:var(--yellow);margin:0;}
  .header .title{font-weight:800;font-size:25px;color:var(--yellow);margin:0;line-height:1.05;white-space:nowrap;}
  .header .since{font-weight:400;font-size:14px;margin:2px 0 0;}
  .photo{position:absolute;left:0;top:100px;}
  .headline{
    position:absolute;left:44px;top:290px;margin:0;font-family:"Fredoka",sans-serif;font-weight:600;
    font-size:30px;line-height:1.12;color:var(--white);
  }
  .headline .hl{color:var(--yellow);}
  .art{position:absolute;border-radius:10px;}
  .art-pencils{left:30px;top:460px;width:82px;height:92px;background:linear-gradient(180deg,#8e5a9e 0%,var(--gold) 45%,var(--gold) 100%);}
  .art-backpack{left:238px;top:500px;width:150px;height:130px;border-radius:40px 40px 18px 18px;background:linear-gradient(180deg,var(--gold) 0%,#4fa3df 60%,var(--gold) 100%);}
  .register{position:absolute;left:410px;top:582px;width:190px;text-align:center;}
  .register .cta{font-family:"Fredoka",sans-serif;font-weight:700;font-size:32px;color:var(--white);line-height:1;margin:0;}
  .register .phone{font-family:"Fredoka",sans-serif;font-weight:600;font-size:26px;color:var(--yellow);margin:6px 0 0;line-height:1.1;}
  .contacts{position:absolute;left:36px;top:712px;right:28px;display:grid;grid-template-columns:1fr 1fr;row-gap:10px;column-gap:20px;font-size:12.5px;color:var(--white);}
  .contact{display:flex;align-items:center;gap:8px;white-space:nowrap;}
  .contact svg{flex:none;}
  .bottom-rule{position:absolute;left:0;bottom:12px;width:100%;height:3px;background:var(--white);}
  .bottom-band{position:absolute;left:0;bottom:0;width:100%;height:12px;background:var(--red);}
</style>
</head>
<body>
<main class="flyer">
  <div class="top-rule"></div>

  <div class="logo-box">
    <span class="logo-dot"></span>
    <span class="logo-name">Maple Nest<br>Child Care &amp; Preschool</span>
  </div>

  <header class="header">
    <p class="lead">A Maple Nest Start to</p>
    <h1 class="title">YOUR CHILD'S FUTURE</h1>
    <p class="since">Quality Education since 2003</p>
  </header>

  <svg class="photo" width="624" height="470" viewBox="0 0 624 470" role="img" aria-label="Photo of a smiling teacher with a group of diverse young children gathered around a tablet">
    <defs>
      <linearGradient id="photoTone" x1="0" y1="0" x2="1" y2="1">
        <stop offset="0" stop-color="#f3d9b8"/>
        <stop offset="0.5" stop-color="#d99a6c"/>
        <stop offset="1" stop-color="#f1b25a"/>
      </linearGradient>
    </defs>
    <path d="M150 0 H624 V425 C600 445 570 440 560 420 C545 450 500 450 488 425 C470 452 420 448 410 420
             C392 446 350 440 345 412 C325 432 290 425 292 398 C265 410 240 392 250 368
             C222 370 205 345 222 322 C195 316 190 285 212 270 C190 258 192 225 216 215
             C180 200 150 175 160 140 C130 130 120 95 140 70 C125 50 130 20 150 0 Z"
          fill="url(#photoTone)" stroke="var(--red)" stroke-width="4"/>
  </svg>

  <h2 class="headline">
    <span class="hl">Let Your</span><br>
    CHILD'S<br>
    <span class="hl">Maple Nest</span><br>
    <span class="hl">Begin</span> TODAY!
  </h2>

  <div class="art art-pencils" role="img" aria-label="Illustration of a yellow cup filled with coloured pencils"></div>
  <div class="art art-backpack" role="img" aria-label="Illustration of a yellow and blue school backpack"></div>

  <div class="register">
    <p class="cta">Register<br>Now</p>
    <p class="phone">555-014-2700</p>
  </div>

  <section class="contacts">
    <div class="contact">
      <svg width="14" height="16" viewBox="0 0 14 16"><path d="M7 0C3.7 0 1 2.6 1 5.9 1 10 7 16 7 16s6-6 6-10.1C13 2.6 10.3 0 7 0zm0 8.2a2.3 2.3 0 110-4.6 2.3 2.3 0 010 4.6z" fill="var(--yellow)"/></svg>
      <span>2140 Willow Lane Fairbrook, IL 60512</span>
    </div>
    <div class="contact">
      <svg width="16" height="16" viewBox="0 0 16 16"><circle cx="8" cy="8" r="6.5" fill="none" stroke="var(--yellow)" stroke-width="1.6"/><path d="M8 4v4.3l2.8 1.7" fill="none" stroke="var(--yellow)" stroke-width="1.6" stroke-linecap="round"/></svg>
      <span>6:30 am – 6:30 pm</span>
    </div>
    <div class="contact">
      <svg width="16" height="16" viewBox="0 0 16 16"><circle cx="8" cy="8" r="7" fill="var(--yellow)"/></svg>
      <span>social.example/MapleNestChildCare</span>
    </div>
    <div class="contact">
      <svg width="16" height="16" viewBox="0 0 16 16" fill="none" stroke="var(--yellow)" stroke-width="1.3"><circle cx="8" cy="8" r="6.5"/><ellipse cx="8" cy="8" rx="3" ry="6.5"/><path d="M1.5 8h13M2.5 4.8h11M2.5 11.2h11"/></svg>
      <span>www.maplenestchildcare.net</span>
    </div>
  </section>

  <div class="bottom-rule"></div>
  <div class="bottom-band"></div>
</main>
</body>
</html>
```